Business Card Design

We are a home improvement and landscaping company based in South Eastern Connecticut hence the name BRIVALE. Landscaping & Home Renovation are our focus. Im looking for a very professional looking design. Something that will intergrade the two perfectly with bright but comfortable colors. The final design should communicate professionalism and trust worthiness in a place people feel most comfortable with their largest investment, that being their home.
Updates

Project Deadline Extended
Reason: I haven't come across a design that satisfies me.

Project Deadline Extended
Reason: Looking for more designs

Industry/Entity Type

Home Improvement

Contact Information for Business Card

Side one will contain my contact information
BRIVALE
Landscaping & Home Renovation
Gerald Matlock
5204139856
HIC.0381957
Side two will have a list of services:
Spring/Fall Clean-Ups
Property Management/Mowing
Lawn Care
Brush Clearing
Design Consultation
Interior Home Improvement
Kitchen, Bath & Office
Basement Finishing/Remodel
Flooring
Drywall
Paint
Doors & Windows
Trim & Base

```html
<!DOCTYPE html>
<html lang="en">
<head>
<meta charset="UTF-8">
<title>BRIVALE Business Card</title>
<link href="https://fonts.googleapis.com/css2?family=Josefin+Slab:wght@400;600&family=Rokkitt:wght@400;500;600&display=swap" rel="stylesheet">
<style>
  :root {
    --stage: #3a3a3a;
    --band: rgba(222, 150, 96, 0.82);
    --band-soft: rgba(226, 160, 110, 0.55);
    --gold: #c98d2c;
    --gold-deep: #b87a22;
    --white: #ffffff;
    --photo-kitchen-a: #8f8778;
    --photo-kitchen-b: #cfc6b6;
    --photo-kitchen-c: #6e665a;
    --photo-room-a: #c9b48e;
    --photo-room-b: #6f7a4e;
    --photo-room-c: #3b3026;
  }
  * { margin: 0; padding: 0; box-sizing: border-box; }
  html, body { width: 1200px; height: 416px; overflow: hidden; background: var(--stage); }
  .canvas { position: relative; width: 1200px; height: 416px; background: var(--stage); }

  .card { position: absolute; top: 56px; width: 532px; height: 303px; overflow: hidden; }
  .card--front { left: 48px; }
  .card--back { left: 632px; }

  .photo { position: absolute; inset: 0; }
  .photo--kitchen {
    background: linear-gradient(100deg, var(--photo-kitchen-b) 0%, var(--photo-kitchen-a) 35%, var(--photo-kitchen-b) 60%, var(--photo-kitchen-c) 100%);
  }
  .photo--living {
    background:
      linear-gradient(180deg, rgba(255,240,210,0.6) 0%, rgba(0,0,0,0) 40%),
      linear-gradient(90deg, var(--photo-room-a) 0%, var(--photo-room-b) 45%, var(--photo-room-a) 75%, var(--photo-room-c) 100%);
  }

  .title-band {
    position: absolute; left: 0; top: 0; width: 100%; height: 97px;
    background: var(--band-soft);
  }
  .brand {
    position: absolute; left: 22px; top: 6px;
    font-family: "Josefin Slab", serif; font-weight: 400;
    font-size: 46px; letter-spacing: 15px; color: var(--white);
  }
  .tagline {
    position: absolute; left: 20px; top: 60px;
    font-family: "Rokkitt", serif; font-weight: 400;
    font-size: 22px; color: var(--white);
  }

  .contact-box {
    position: absolute; left: 109px; top: 194px; width: 181px; height: 109px;
    background: linear-gradient(180deg, var(--gold) 0%, var(--gold-deep) 100%);
    text-align: right; padding: 20px 11px 0 0; color: var(--white);
    font-family: "Rokkitt", serif;
  }
  .contact-name { font-size: 22px; font-weight: 600; line-height: 26px; }
  .contact-line { font-size: 14px; line-height: 19px; }

  .services {
    position: absolute; list-style: none; background: var(--band);
    font-family: "Rokkitt", serif; font-size: 15.5px; color: var(--white); line-height: 22.8px;
  }
  .services--left { left: 0; top: 16px; width: 328px; padding: 4px 0 6px 14px; }
  .services--right { right: 0; top: 174px; width: 336px; padding: 8px 14px 6px 0; text-align: right; }
</style>
</head>
<body>
<div class="canvas">
  <section class="card card--front">
    <div class="photo photo--kitchen" role="img" aria-label="Photo of a modern stone and concrete kitchen interior"></div>
    <div class="title-band">
      <div class="brand">BRIVALE</div>
      <div class="tagline">Landscaping &amp; Home Renovation</div>
    </div>
    <div class="contact-box">
      <div class="contact-name">Gerald Matlock</div>
      <div class="contact-line">52041 39856</div>
      <div class="contact-line">HIC. 0381957</div>
    </div>
  </section>

  <section class="card card--back">
    <div class="photo photo--living" role="img" aria-label="Photo of a bright living room with large windows onto a garden"></div>
    <ul class="services services--left">
      <li>- Spring/Fall Clean-Ups Property Management</li>
      <li>- Mowing Lawn Care</li>
      <li>- Brush Clearing</li>
      <li>- Design Consultation</li>
      <li>- Interior Home Improvement Kitchen</li>
    </ul>
    <ul class="services services--right">
      <li>- Bath &amp; Office Basement Finishing</li>
      <li>- Remodel Flooring</li>
      <li>- Drywall Paint</li>
      <li>- Doors &amp; Windows Trim &amp; Base</li>
    </ul>
  </section>
</div>
</body>
</html>
```